Local fast-growing company in the service sector

We are looking for a modern business card design, which should also appear on our letterheads

Target Market(s)

Private and industrial sectors

Contact Information for Business Card

Vorname Name
Lindkofer Str. 18
71468 Remsfeld
Tel.: 07163-418259-0
Name@kovaltec-pbz.de

Colors
9d9d9d
919191
aaaaaa

Requirements
Must have
• The logo (file) in silver

```html
<!DOCTYPE html>
<html lang="de">
<head>
<meta charset="utf-8">
<title>PBZ Business Card</title>
<link rel="stylesheet" href="https://fonts.googleapis.com/css2?family=Roboto:wght@400;500;700&family=Roboto+Condensed:wght@700&display=swap">
<style>
  :root {
    --canvas: #e4e2df;
    --card-black: #0b0b0b;
    --card-black-hi: #2a2a2a;
    --silver-light: #f2f2f2;
    --silver: #aaaaaa;
    --silver-mid: #9d9d9d;
    --silver-dark: #919191;
    --text-light: #d8d8d8;
    --text-muted: #9d9d9d;
  }
  * { margin: 0; padding: 0; box-sizing: border-box; }
  html, body { width: 1200px; height: 1023px; overflow: hidden; }
  body {
    background: var(--canvas);
    font-family: "Roboto", Arial, sans-serif;
    display: flex;
    flex-direction: column;
    align-items: center;
    justify-content: center;
    gap: 60px;
  }
  .card {
    width: 620px;
    height: 354px;
    border-radius: 18px;
    position: relative;
    overflow: hidden;
    box-shadow: 0 10px 30px rgba(0,0,0,0.25);
  }
  .card--front {
    background: linear-gradient(160deg, var(--card-black-hi) 0%, var(--card-black) 45%, #000 100%);
    color: var(--text-light);
  }
  .brand {
    position: absolute;
    left: 48px;
    top: 46px;
    display: flex;
    align-items: center;
    gap: 16px;
  }
  .brand__square {
    width: 44px;
    height: 44px;
    background: var(--silver);
  }
  .brand__text { display: flex; flex-direction: column; }
  .brand__name {
    font-family: "Roboto Condensed", Arial, sans-serif;
    font-weight: 700;
    font-size: 64px;
    line-height: 0.9;
    color: var(--silver-light);
    letter-spacing: 1px;
  }
  .brand__web {
    font-size: 17px;
    color: var(--silver);
    margin-top: 4px;
    letter-spacing: 0.5px;
  }
  .person {
    position: absolute;
    left: 48px;
    top: 168px;
  }
  .person__name {
    font-size: 26px;
    font-weight: 500;
    color: var(--silver-light);
    letter-spacing: 0.5px;
  }
  .person__role {
    font-size: 13px;
    color: var(--text-muted);
    letter-spacing: 1px;
    margin-top: 2px;
  }
  .contact {
    position: absolute;
    left: 48px;
    top: 236px;
    font-size: 17px;
    line-height: 1.3;
    color: var(--text-light);
  }
  .contact__line { display: flex; align-items: center; gap: 10px; }
  .contact__gap { height: 8px; }
  .contact__icon { width: 13px; height: 13px; fill: none; stroke: var(--text-light); stroke-width: 1.6; }
  .card--back {
    background: linear-gradient(135deg, var(--silver-light) 0%, #d6d6d6 40%, var(--silver) 75%, var(--silver-dark) 100%);
    display: flex;
    align-items: center;
    justify-content: center;
    gap: 22px;
  }
  .card--back .brand__square { width: 70px; height: 70px; background: var(--silver-dark); }
  .back-name {
    font-family: "Roboto Condensed", Arial, sans-serif;
    font-weight: 700;
    font-size: 110px;
    color: #7d7d7d;
    letter-spacing: 2px;
  }
</style>
</head>
<body>
  <section class="card card--front" aria-label="Visitenkarte Vorderseite">
    <div class="brand">
      <div class="brand__square"></div>
      <div class="brand__text">
        <span class="brand__name">PBZ</span>
        <span class="brand__web">kovaltec-pbz.de</span>
      </div>
    </div>
    <div class="person">
      <p class="person__name">MAREK LINDNER</p>
      <p class="person__role">DIRECTOR</p>
    </div>
    <div class="contact">
      <p class="contact__line">Lindkofer Str. 18</p>
      <p class="contact__line">71468 Remsfeld</p>
      <div class="contact__gap"></div>
      <p class="contact__line">
        <svg class="contact__icon" viewBox="0 0 14 14"><path d="M3 1.5 L5.5 4 L4.3 5.6 Q6 8.5 8.4 9.7 L10 8.5 L12.5 11 L11 12.5 Q5 12 1.5 3 Z"/></svg>
        07163-418259-0
      </p>
      <p class="contact__line">
        <svg class="contact__icon" viewBox="0 0 14 14"><rect x="1" y="3" width="12" height="8"/><path d="M1 3 L7 8 L13 3"/></svg>
        Name@kovaltec-pbz.de
      </p>
    </div>
  </section>

  <section class="card card--back" aria-label="Visitenkarte Rückseite">
    <div class="brand__square"></div>
    <span class="back-name">PBZ</span>
  </section>
</body>
</html>
```